The Wormwick Papers Theatre Production Poster

We're after a poster for a theatre production based on D.R Kellam's book, The Wormwick Papers.
This play follows the story of a senior demon teaching a student demon how to tempt humankind. The tone of the play is light and formal with dark undertones and moments of levity. Hell is set in a university. I am wanting an eye-catching poster. Something subtle and NOT in the theme of 'horror'. I am open to different creative ideas, but I like the idea of a book being involved and maybe some shadow loosely representing a demon reading the book. Another idea could be a shadow hovering over a silhouetted human.
Other details that the poster must include:
- The Name of the Show: The Wormwick Papers
- Time of the shows: 7:30 pm
- Dates of the show: Saturday 8th and 15th of October 2022
- Location: Pembrook Civic Theatre
- Organisation: Lantern Theatre Productions
- ticket price: $38
- bookings made at: https://app.seatbooker-example.org.au/LanternTheatreProductions/Wormwick
Target Market(s)
university Students
Industry/Entity Type
Theatre
Look and feel

```html
<!DOCTYPE html>
<html lang="en">
<head>
<meta charset="utf-8">
<title>The Wormwick Papers – Lantern Theatre Productions</title>
<link rel="stylesheet" href="https://fonts.googleapis.com/css2?family=Encode+Sans+Condensed:wght@400;600&family=Kaushan+Script&display=swap">
<style>
  :root {
    --page-bg: #ebebeb;
    --olive-dark: #45430f;
    --olive-mid: #6b6818;
    --olive-light: #8c8820;
    --shadow-yellow: #b5ae25;
    --magenta: #a3236b;
    --title-yellow: #f6e81c;
    --label-bg: #2b2929;
    --label-text: #f3f3f3;
  }
  * { margin: 0; padding: 0; box-sizing: border-box; }
  html, body { width: 1200px; height: 960px; overflow: hidden; background: var(--page-bg); }
  .poster {
    position: absolute; left: 280px; top: 28px; width: 640px; height: 904px;
    overflow: hidden; font-family: "Encode Sans Condensed", "Arial Narrow", sans-serif;
  }
  .poster-art { position: absolute; inset: 0; width: 100%; height: 100%; }
  .presenter {
    position: absolute; left: 383px; top: 209px; width: 234px;
    display: flex; flex-direction: column; align-items: center;
  }
  .presenter span {
    background: var(--label-bg); color: var(--label-text);
    font-size: 25px; line-height: 34px; padding: 0 5px; text-transform: uppercase;
    letter-spacing: -0.5px; white-space: nowrap;
  }
  .title {
    position: absolute; inset: 0; pointer-events: none;
    font-family: "Kaushan Script", cursive; font-weight: 400; color: var(--title-yellow);
    text-shadow: 3px 4px 4px rgba(0,0,0,0.55);
  }
  .title .line { position: absolute; display: block; line-height: 1; white-space: nowrap; }
  .title .the { left: 150px; top: 172px; font-size: 112px; }
  .title .name { left: 40px; width: 550px; top: 280px; font-size: 112px; text-align: center; }
  .title .papers { left: 120px; width: 380px; top: 400px; font-size: 118px; text-align: center; }
  .label { position: absolute; background: var(--label-bg); color: var(--label-text); white-space: nowrap; }
  .dates { left: 177px; top: 583px; width: 346px; height: 70px; font-size: 52px; line-height: 70px; text-align: center; letter-spacing: -0.5px; }
  .year-venue { left: 177px; top: 674px; width: 348px; height: 84px; display: flex; align-items: center; justify-content: center; }
  .year { font-size: 80px; line-height: 84px; letter-spacing: -2px; }
  .venue { font-size: 29px; line-height: 30px; text-align: center; margin-left: 6px; letter-spacing: -0.5px; }
  .tickets { left: 218px; top: 757px; width: 292px; height: 34px; font-size: 20px; font-weight: 600; line-height: 34px; text-align: center; letter-spacing: -0.3px; }
  .bookings { left: 44px; top: 813px; width: 552px; height: 28px; font-size: 13px; line-height: 28px; text-align: center; }
</style>
</head>
<body>
<main class="poster">
  <svg class="poster-art" viewBox="0 0 640 904" role="img" aria-label="Artwork: yellow shadow silhouettes of a man and a horned demon looming over a magenta human figure, on a grainy olive ground">
    <defs>
      <linearGradient id="groundGradient" x1="0" y1="0" x2="1" y2="1">
        <stop offset="0" stop-color="var(--olive-mid)"/>
        <stop offset="0.5" stop-color="var(--olive-light)"/>
        <stop offset="1" stop-color="var(--olive-dark)"/>
      </linearGradient>
      <filter id="softEdge" x="-20%" y="-20%" width="140%" height="140%">
        <feGaussianBlur stdDeviation="18"/>
      </filter>
    </defs>
    <rect width="640" height="904" fill="url(#groundGradient)"/>
    <g filter="url(#softEdge)">
      <rect x="10" y="80" width="210" height="800" rx="60" fill="var(--shadow-yellow)" opacity="0.85"/>
      <rect x="360" y="40" width="280" height="640" rx="70" fill="var(--shadow-yellow)" opacity="0.85"/>
      <rect x="280" y="260" width="150" height="640" rx="60" fill="var(--magenta)" opacity="0.85"/>
    </g>
  </svg>

  <p class="presenter"><span>Lantern Theatre</span><span>Productions presents</span></p>

  <h1 class="title">
    <span class="line the">The</span>
    <span class="line name">Wormwick</span>
    <span class="line papers">Papers</span>
  </h1>

  <p class="label dates">8 &amp; 15 October</p>
  <p class="label year-venue"><span class="year">2022</span><span class="venue">Pembrook Civic<br>Theatre</span></p>
  <p class="label tickets">Tickets $38.00, show starts 7.30pm</p>
  <p class="label bookings">Bookings made at: https://app.seatbooker-example.org.au/LanternTheatreProductions/Wormwick</p>
</main>
</body>
</html>
```